依頼概要
■概要
鳥取県の片田舎の高齢者による農事生産組合の初挑戦に力をお貸しください。来春発売予定の古代米酒「翠嶺之花(すいれいのはな)」のラベルと化粧箱のデザインをお願いします。

■古事記神話由来の水で育てた古代米を日本酒に!
鳥取県西伯郡南部町清水川には、八十神(やそがみ)に赤猪に似せた焼いた岩を落とされて、それを抱きとめて絶命した若き日の大国主命が、母神の願いで遣わされたキサガイ姫(比売)、ウムギ姫の薬によって蘇生復活し、さらに丈夫になったという古事記再生神話が伝わっています。その大国主命を蘇生復活させた薬を練ったと伝わる鶴舞岩という泉があり、今まで一度も涸れたことがありません。
その泉の水が流れ込む田で育てた古代米アカツキモチ(黒米)を使って日本酒を作り、2017年春より販売することになりました。

■大国主命の神楽を奉納する貴重な古代米
古代米の圃場はわずか5アールしかありません。収穫できる米はたったの2俵ほどです。そして、春の田植えでは大国主命の神楽を舞い、大国主命が古代米の苗を田に投げ入れて手植えで田植えをしています。また、秋の稲刈りでも神楽を舞って収穫に感謝しています。そのありがたく貴重な古代米が日本酒になるのです。

■限定1800本の高級酒
神話由来の古代米から醸造できる古代米酒は、わずか1800本です。そのため販売価格は720mlで2500円を予定しています。瓶はすりガラスで細め、古代米酒の色は透明度の高い琥珀色になります。
商品名は「翠嶺之花(すいれいのはな)」になりますが、比売神とは姫神のことです。

■販売ターゲット
古事記神話に興味のある方、とくに20~40代の女性、スピリチュアルなもの、パワースポットなどが好きな方、鶴舞岩を訪れた方、田植えや稲刈りに参加された方。

■販売方法
ふるさと納税返礼品、近隣の道の駅、駅、空港、インターネット販売など。フランスなどの海外での販売の可能性があります。

■デザインへの要望
価格、販売ターゲット、販売方法を考慮して、それにふさわしい高級感のあるお洒落なデザインを希望します。類似商品との差別化として、古事記神話由来の水で造った古代米酒であることをPRしたいです。

■備考
・当方は田舎の高齢者による農事生産組合であるため、専門的な知識がなく質問への返答など的外れになりましたら申し訳ありません。
・古事記再生神話、キサガイ姫、ウムギ姫、大国主命などについて調べていただいて、そこからイマジネーションを拡げていただくのもよいかもしれません。
・デザイン採用後に微調整程度の細かい修正をお願いする場合があります。(大きな修正の場合は、別途報酬を支払います)
・デザインされた図案についてはホームページやチラシ等で一部変更などして使用させていただく場合がありますので著作権の買取とさせていただきます。
・その代わりとしてですが、採用された場合、デザイン実績、成果物として公表していただいて構いません。
・新発売前にクラウドファンディングを行う予定です。

これまでの取組みにつきましては、下記のホームページを参考にしてください。
http://hoshi.tenrab.example/category/farm-plan-notes/

また、facebookページに最新情報もありますので、チェックしてみてください。
https://www.palnook.example/turumaiwa/

60代以上の高齢者の農事生産組合ではじめての取組みでした。
年寄りの観点ではいけないということで、以前から農作業を手伝っていただいている湊嶺大学の学生ボランティアのみなさんに応募作品を全部送って選んでもらったところ、今回のデザインへの支持が多くあり、それに決定しました。
若い女性の感性でこれに決まったということになります。

応募していただいたみなさま、本当にありがとうございました。
応募作のすべてがとてもよいデザインで、本当に悩みました。
今後もまた募集させていただくこともあるかと思いますので、その際はよろしくお願いいたします。

鳥取県南部町という田舎ですが、古事記神話の上巻では大国主命や八十神、毘女神が活躍する舞台です。
是非、遊びに来ていただければと思います。

応募していただいたみなさま、検討していただいたみなさま、本当にありがとうございました。

```html
<!DOCTYPE html>
<html lang="ja">
<head>
<meta charset="utf-8">
<title>翠嶺之花 ラベル</title>
<link rel="stylesheet" href="https://fonts.googleapis.com/css2?family=Shippori+Mincho:wght@500;700&family=Yuji+Boku&family=Cormorant+Garamond:wght@500&display=swap">
<style>
  :root {
    --page-bg: #eef0f2;
    --label-sky-top: #6fc3ec;
    --label-sky-bottom: #9ed8f4;
    --drop-fill: #ffffff;
    --drop-line: #1a1a1a;
    --ink: #151515;
    --accent-blue: #1f6fc0;
  }
  * { margin: 0; padding: 0; box-sizing: border-box; }
  html, body {
    width: 1200px;
    height: 3224px;
    overflow: hidden;
    background: var(--page-bg);
  }
  .label {
    position: absolute;
    left: 160px;
    top: 1112px;
    width: 880px;
    height: 1000px;
    overflow: hidden;
  }
  .label__ripples {
    position: absolute;
    inset: 0;
    background: linear-gradient(180deg, var(--label-sky-top) 0%, var(--label-sky-bottom) 55%, var(--label-sky-top) 100%);
  }
  .label__drop {
    position: absolute;
    inset: 0;
  }
  .vertical {
    position: absolute;
    writing-mode: vertical-rl;
    color: var(--ink);
    font-family: "Shippori Mincho", serif;
    font-weight: 500;
  }
  .origin {
    left: 580px;
    top: 150px;
    font-size: 36px;
    letter-spacing: 4px;
  }
  .rice-note {
    left: 258px;
    top: 200px;
    font-size: 36px;
    letter-spacing: 4px;
  }
  .sake-class {
    left: 500px;
    top: 300px;
    font-size: 32px;
    letter-spacing: 6px;
  }
  .product-name {
    left: 376px;
    top: 330px;
    font-family: "Yuji Boku", serif;
    font-weight: 400;
    font-size: 116px;
    line-height: 1.1;
    letter-spacing: -4px;
  }
  .product-dot {
    position: absolute;
    left: 488px;
    top: 760px;
    width: 34px;
    height: 34px;
    border-radius: 50%;
    background: var(--accent-blue);
  }
  .product-roman {
    position: absolute;
    left: 0;
    width: 880px;
    top: 812px;
    text-align: center;
    font-family: "Cormorant Garamond", serif;
    font-weight: 500;
    font-size: 26px;
    line-height: 1.15;
    letter-spacing: 3px;
    color: var(--ink);
  }
</style>
</head>
<body>
  <main class="label">
    <div class="label__ripples" role="img" aria-label="水面に広がる波紋の模様"></div>
    <svg class="label__drop" width="880" height="1000" viewBox="0 0 880 1000" aria-hidden="true">
      <path d="M440 0 C450 300 660 520 660 720 A220 220 0 0 1 220 720 C220 520 430 300 440 0 Z"
            fill="var(--drop-fill)" stroke="var(--drop-line)" stroke-width="4"/>
    </svg>
    <p class="vertical origin">鳥取県白峰川</p>
    <p class="vertical rice-note">古代米使用酒</p>
    <p class="vertical sake-class">清酒</p>
    <h1 class="vertical product-name">翠嶺之花</h1>
    <span class="product-dot"></span>
    <p class="product-roman">SUIREI<br>no<br>HANA</p>
  </main>
</body>
</html>
```